On going F&B business needs a new stationery design for festive occasion

Would like something like the attached file, but with a new look. The basis colours should still be green and yellow.

```html
<!DOCTYPE html>
<html lang="en">
<head>
<meta charset="utf-8">
<title>Al - Bahar Dining Corner – Business Card</title>
<link rel="stylesheet" href="https://fonts.googleapis.com/css2?family=Montserrat:wght@700&family=Roboto:wght@400;500&display=swap">
<style>
  :root {
    --backdrop: #d4d5d7;
    --card-white: #ffffff;
    --brand-green: #044f27;
    --brand-yellow: #f2ea3a;
    --text-grey: #555555;
    --faint-green: #1d6336;
  }
  * { box-sizing: border-box; margin: 0; padding: 0; }
  html, body {
    width: 1200px; height: 1200px; overflow: hidden;
    background: var(--backdrop);
  }
  .card {
    position: absolute; left: 192px; width: 816px; height: 465px;
    border-radius: 7px; overflow: hidden;
  }
  .card-front { top: 125px; background: var(--card-white); }
  .card-back { top: 610px; background: var(--brand-green); }

  .brand { position: absolute; display: flex; align-items: center; }
  .brand-dot { border-radius: 50%; flex: none; }
  .brand-name {
    font-family: "Montserrat", sans-serif; font-weight: 700;
    line-height: 1.15; text-align: center;
  }
  .card-front .brand { left: 78px; top: 182px; gap: 16px; }
  .card-front .brand-dot { width: 60px; height: 60px; background: var(--brand-green); }
  .card-front .brand-name { color: var(--brand-green); font-size: 27px; }
  .card-front .brand-name .line-sub { font-size: 20px; }

  .divider {
    position: absolute; left: 406px; top: 132px; width: 3px; height: 200px;
    background: var(--brand-green);
  }
  .contact { position: absolute; left: 446px; top: 124px; }
  .person-name {
    font-family: "Montserrat", sans-serif; font-weight: 700;
    font-size: 29px; color: var(--brand-green); letter-spacing: 0.3px;
  }
  .person-role {
    font-family: "Roboto", sans-serif; font-weight: 500;
    font-size: 24px; color: var(--text-grey); margin-top: 2px;
  }
  .contact-list { list-style: none; margin-top: 16px; }
  .contact-list li {
    display: flex; align-items: center; gap: 8px; height: 31.5px;
    font-family: "Roboto", sans-serif; font-size: 23px; color: var(--text-grey);
  }
  .contact-list svg { width: 20px; height: 20px; fill: var(--brand-green); flex: none; }

  .address {
    position: absolute; left: 0; right: 0; top: 360px; text-align: center;
    font-family: "Roboto", sans-serif; font-size: 22px; line-height: 30px;
    color: var(--text-grey);
  }

  .back-accent {
    position: absolute; left: 456px; top: 74px; width: 360px; height: 360px;
    border-radius: 50%; background: var(--faint-green); opacity: 0.5;
  }
  .card-back .brand { left: 150px; top: 150px; gap: 26px; }
  .card-back .brand-dot { width: 104px; height: 104px; background: var(--brand-yellow); }
  .card-back .brand-name { color: var(--brand-yellow); font-size: 56px; }
  .card-back .brand-name .line-sub { font-size: 38px; }
</style>
</head>
<body>
  <section class="card card-front">
    <div class="brand">
      <span class="brand-dot"></span>
      <div class="brand-name">AL - BAHAR<br><span class="line-sub">DINING CORNER</span></div>
    </div>
    <div class="divider"></div>
    <div class="contact">
      <div class="person-name">RASHID KARIM</div>
      <div class="person-role">Director</div>
      <ul class="contact-list">
        <li><svg viewBox="0 0 20 20" aria-hidden="true"><path d="M2 7c0-3 4-4 8-4s8 1 8 4v2h-4V7H6v2H2z"/><path d="M5 10h10l2 7H3z"/></svg>91827364</li>
        <li><svg viewBox="0 0 20 20" aria-hidden="true"><path d="M5 2h10v5H5z"/><path d="M2 8h16v7h-3v-3H5v3H2z"/><path d="M6 13h8v5H6z"/></svg>6210 4389</li>
        <li><svg viewBox="0 0 20 20" aria-hidden="true"><path d="M2 4h16v12H2z M3.5 5.5v1l6.5 5 6.5-5v-1z" fill-rule="evenodd"/></svg>rkx21@mailbox.example.sg</li>
        <li><svg viewBox="0 0 20 20" aria-hidden="true"><circle cx="10" cy="10" r="9"/><path d="M6 5c2 1 3 2 2 4s1 3 0 5M13 4c-1 2 1 3 2 4s-1 4-2 5" stroke="#fff" stroke-width="1.5" fill="none"/></svg>www.al-bahar.example.sg</li>
      </ul>
    </div>
    <p class="address">18, Harbourline Industrial Park Road<br>#02-07 Singapore 700123.</p>
  </section>

  <section class="card card-back">
    <div class="back-accent"></div>
    <div class="brand">
      <span class="brand-dot"></span>
      <div class="brand-name">AL - BAHAR<br><span class="line-sub">DINING CORNER</span></div>
    </div>
  </section>
</body>
</html>
```